Start out business card needed

We have uploaded a flyer we like the design of for inspiration for the business card.

Target Market(s)

Fitness lovers

Industry/Entity Type

Health And Wellness

Contact Information for Business Card

Business Development Manager
Rik ten holtebrink
Phone number to be advised
Rik@pulse-yard.com.au
www.pulse-yard.com.au

Font styles to use
Sans Serif

Colors
fbee3e
1b1b1b
f5f5f5

Requirements
Must have
• Front : Logo (large should take up most of the space)
• Back : small logo, business details

```html
<!DOCTYPE html>
<html lang="en">
<head>
<meta charset="utf-8">
<title>Pulse Yard – Business Cards</title>
<link href="https://fonts.googleapis.com/css2?family=Roboto+Condensed:wght@400;700&display=swap" rel="stylesheet">
<style>
  :root {
    --yellow: #fbee3e;
    --ink: #1b1b1b;
    --paper: #f5f5f5;
    --stage: #2b2b2b;
    --photo-light: #5a5a5a;
  }
  * { margin: 0; padding: 0; box-sizing: border-box; }
  html, body {
    width: 1200px; height: 880px; overflow: hidden;
    background: var(--stage);
    font-family: "Roboto Condensed", Arial, sans-serif;
  }
  .canvas { position: relative; width: 1200px; height: 880px; }

  .card {
    position: absolute; width: 620px; height: 344px; overflow: hidden;
    box-shadow: 0 18px 40px rgba(0,0,0,.55);
  }

  /* Front */
  .card-front { left: 60px; top: 60px; background: var(--ink); }
  .front-photo {
    position: absolute; right: 0; top: 0; width: 340px; height: 344px;
    background: radial-gradient(ellipse at 55% 40%, var(--photo-light) 0%, #333 40%, var(--ink) 75%);
    opacity: .8;
  }
  .front-logo {
    position: absolute; left: 0; right: 0; top: 118px;
    display: flex; align-items: center; justify-content: center; gap: 18px;
  }
  .front-logo .mark-square { width: 26px; height: 26px; background: var(--yellow); }
  .front-logo .wordmark {
    color: var(--yellow); font-weight: 700; font-size: 78px;
    letter-spacing: 4px; line-height: 1;
  }
  .front-web {
    position: absolute; left: 0; right: 0; top: 236px; text-align: center;
    color: var(--yellow); font-size: 15px; letter-spacing: 2px;
  }

  /* Back */
  .card-back { left: 520px; top: 476px; background: var(--yellow); }
  .back-band { position: absolute; inset: 0; }
  .back-logo {
    position: absolute; left: 0; right: 0; top: 62px;
    display: flex; align-items: center; justify-content: center; gap: 12px;
  }
  .back-logo .mark-square { width: 16px; height: 16px; background: var(--ink); }
  .back-logo .wordmark {
    color: var(--ink); font-weight: 700; font-size: 48px; letter-spacing: 3px; line-height: 1;
  }
  .holder { position: absolute; left: 0; right: 0; top: 140px; text-align: center; color: var(--ink); }
  .holder-name { font-size: 24px; letter-spacing: .5px; text-transform: uppercase; }
  .holder-name .first { font-weight: 400; }
  .holder-name .last { font-weight: 700; }
  .holder-role { font-size: 15px; margin-top: 2px; }

  .contact { position: absolute; color: var(--yellow); display: flex; align-items: center; gap: 8px; }
  .contact svg { fill: var(--yellow); }
  .contact-email { left: 372px; top: 220px; font-size: 18px; }
  .contact-phone { left: 36px; top: 276px; font-size: 22px; letter-spacing: .5px; }
  .contact-web { left: 360px; top: 282px; font-size: 15px; letter-spacing: 1.5px; }
</style>
</head>
<body>
<main class="canvas">

  <section class="card card-front" aria-label="Card front">
    <div class="front-photo" role="img" aria-label="Moody black and white photo of a boxer with raised gloves"></div>
    <div class="front-logo">
      <span class="mark-square"></span>
      <span class="wordmark">PULSE YARD</span>
    </div>
    <p class="front-web">www.pulse-yard.com.au</p>
  </section>

  <section class="card card-back" aria-label="Card back">
    <svg class="back-band" width="620" height="344" viewBox="0 0 620 344" aria-hidden="true">
      <polygon points="0,262 296,262 314,244 344,244 356,208 620,208 620,344 0,344" fill="var(--ink)"/>
      <rect x="0" y="318" width="620" height="6" fill="var(--yellow)"/>
    </svg>

    <div class="back-logo">
      <span class="mark-square"></span>
      <span class="wordmark">PULSE YARD</span>
    </div>

    <div class="holder">
      <p class="holder-name"><span class="first">Rik</span> <span class="last">ten holtebrink</span></p>
      <p class="holder-role">Business Development Manager</p>
    </div>

    <p class="contact contact-email">
      <svg width="20" height="14" viewBox="0 0 20 14" aria-hidden="true"><path d="M0 0h20v14H0z M2 2v10h16V2l-8 6z" fill-rule="evenodd"/></svg>
      Rik@pulse-yard.com.au
    </p>
    <p class="contact contact-phone">
      0412555019
      <svg width="20" height="18" viewBox="0 0 20 18" aria-hidden="true"><path d="M1 5c0-3 4-4 9-4s9 1 9 4v2h-5V5H6v2H1z M4 9h12l2 8H2z"/></svg>
    </p>
    <p class="contact contact-web">www.pulse-yard.com.au</p>
  </section>

</main>
</body>
</html>
```